Tarn - Stationary Design/Layout

We are a well established clothing design and manufacturing company (Tarn Sourcing) based in London UK, with our own factory in Bangladesh, supplying to many fashion retailers and brands. Our factory has very high environmental and ethical standards with people at its heart. Our quality of garments are second to none.
Our new logo has been proudly developed by the Pixel Guild community last month, we are now in the second phase and need the layout designed for our letterheads, double sided business cards, compliment slip and clothing ticket. Feel as creative as you like, but make sure it looks great!!
***The Logo - the logo design and colour is set and should NOT be changed and stay on a dark grey backround. The logo artwork to use is attached.
***Details to use for the business card:
Dorian Pelham
Direct Line: 020 7946 0158
dorian@tarnsourcing-example.com
Tarn Sourching Ltd.
57 - 59 Hollin Row
Harlow . Kestby
NW9 4QT
Switchboard: 020 7946 0274
Fax: 020 7946 0274
www.tarnsourcing-example.co.uk
***Details to use for the letterhead and compliment slip:
Tarn Sourching Ltd.
57 - 59 Hollin Row
Harlow . Kestby
NW9 4QT
Fax: 020 7946 0274
www.tarnsourcing-example.co.uk
***Details for Swing Ticket:
Size: 12cm height by 5.5cm width
One side need to have just the logo without the 'Sourcing', on the other it needs to stay blank

```html
<!DOCTYPE html>
<html lang="en">
<head>
<meta charset="utf-8">
<title>Tarn Sourcing – Stationery Set</title>
<link rel="stylesheet" href="https://fonts.googleapis.com/css2?family=Questrial&display=swap">
<style>
  :root {
    --backdrop: #8b4a27;
    --paper: #ffffff;
    --card-white: #f4f4f4;
    --brand-dark: #2e2e2e;
    --brand-dark-light: #4d4d4d;
    --brand-accent: #a9dde2;
    --ink: #333333;
    --heading-ink: #222222;
  }
  * { margin: 0; padding: 0; box-sizing: border-box; }
  html, body { width: 1200px; height: 822px; overflow: hidden; }
  body {
    position: relative;
    background: var(--backdrop);
    font-family: "Questrial", "Century Gothic", sans-serif;
    color: var(--ink);
  }
  .sheet { position: absolute; background: var(--paper); box-shadow: 0 2px 6px rgba(0,0,0,.35); }
  .brand-block {
    position: absolute;
    background: linear-gradient(135deg, var(--brand-dark-light), var(--brand-dark));
    display: flex; align-items: center; justify-content: center;
    color: var(--brand-accent);
    font-weight: 400;
    white-space: nowrap;
    letter-spacing: .04em;
  }
  .details { position: absolute; font-size: 8px; line-height: 1.35; white-space: nowrap; font-weight: 400; }

  /* Letterhead */
  .letterhead { left: 46px; top: 64px; width: 544px; height: 699px; }
  .letterhead .brand-block { left: 0; top: 18px; width: 152px; height: 55px; font-size: 17px; }
  .letterhead .address { left: 275px; top: 24px; }
  .letterhead .contact { left: 410px; top: 24px; }

  /* Business card front */
  .card-front { left: 612px; top: 73px; width: 223px; height: 128px; border-radius: 6px; overflow: hidden; }
  .card-front .brand-block { inset: 0; font-size: 22px; }

  /* Business card back */
  .card-back { left: 853px; top: 73px; width: 225px; height: 128px; background: var(--card-white); border-radius: 6px; }
  .card-back .brand-block { left: 0; top: 22px; width: 100px; height: 34px; font-size: 11px; }
  .card-back .address { left: 6px; top: 62px; font-size: 6px; line-height: 1.3; }
  .card-back .person { right: 8px; top: 96px; text-align: right; font-size: 6px; line-height: 1.4; }
  .card-back .person-name { font-size: 9px; }

  /* Compliment slip */
  .comp-slip { left: 608px; top: 219px; width: 542px; height: 179px; }
  .comp-slip .brand-block { left: 40px; top: 31px; width: 205px; height: 79px; font-size: 28px; }
  .comp-slip .heading {
    position: absolute; left: 283px; top: 56px;
    font-size: 22px; font-weight: 400; letter-spacing: .02em;
    color: var(--heading-ink); white-space: nowrap;
  }
  .comp-slip .address { left: 32px; top: 121px; }
  .comp-slip .contact { left: 140px; top: 121px; }

  /* Swing ticket front */
  .ticket-front { left: 608px; top: 424px; width: 301px; height: 137px; }
  .ticket-front .brand-block { inset: 0; font-size: 30px; letter-spacing: .08em; }

  /* Envelope */
  .envelope { left: 608px; top: 584px; width: 301px; height: 141px; }
  .envelope .brand-block { left: 0; top: 4px; width: 72px; height: 32px; font-size: 9px; }
</style>
</head>
<body>

<section class="sheet letterhead" aria-label="Letterhead">
  <div class="brand-block">Tarn Sourcing</div>
  <div class="details address">Tarn Sourching Ltd.<br>57 - 59 Hollin Row<br>Harlow . Kestby<br>NW9 4QT</div>
  <div class="details contact">Switchboard: 020 7946 0274<br>Fax: 020 7946 0274<br>www.tarnsourcing-example.co.uk</div>
</section>

<section class="sheet card-front" aria-label="Business card front">
  <div class="brand-block">Tarn Sourcing</div>
</section>

<section class="sheet card-back" aria-label="Business card back">
  <div class="brand-block">Tarn Sourcing</div>
  <div class="details address">Tarn Sourching Ltd.<br>57 - 59 Hollin Row<br>Harlow . Kestby<br>NW9 4QT<br>Switchboard: 020 7946 0274<br>Fax: 020 7946 0274<br>www.tarnsourcing-example.co.uk</div>
  <div class="details person"><span class="person-name">Dorian Pelham</span><br>Direct Line: 020 7946 0158<br>dorian@tarnsourcing-example.com</div>
</section>

<section class="sheet comp-slip" aria-label="Compliment slip">
  <div class="brand-block">Tarn Sourcing</div>
  <h2 class="heading">WITH COMPLIMENTS</h2>
  <div class="details address">Tarn Sourching Ltd.<br>57 - 59 Hollin Row<br>Harlow . Kestby<br>NW9 4QT</div>
  <div class="details contact">Switchboard: 020 7946 0274<br>Fax: 020 7946 0274<br>www.tarnsourcing-example.co.uk</div>
</section>

<section class="sheet ticket-front" aria-label="Swing ticket">
  <div class="brand-block">Tarn</div>
</section>

<section class="sheet envelope" aria-label="Envelope">
  <div class="brand-block">Tarn Sourcing</div>
</section>

</body>
</html>
```